Harlow Stonefield Civil Construction website design

We want a Bold website to promote our Heavy Civil Construction company, We would like an organic / tangible feel to the site. The pictures will be over saturated so they pop. We need to be able to easliy upload new projects and pictures on a regular basis.
Home page will have a full screen width image, "home page image" with silhouette and logo. It will also have about us area and picture
Page 2 will be Project Gallery with pictures in project folders
Page 3 will be an employment application form and submission
Page 4 will be Contact Us
Target Market(s)
Construction indusrty
Industry/Entity Type
Contractor
Coding
Coded - Design and coding required
Number of Pages Required
4 page
Font styles to use
Other font styles liked:
- Hypatia Sans Pro Light
Look and feel

```html
<!DOCTYPE html>
<html lang="en">
<head>
<meta charset="utf-8">
<title>Harlow Stonefield Civil Construction</title>
<link rel="stylesheet" href="https://fonts.googleapis.com/css2?family=Montserrat:wght@300;400;500;600;700;900&family=Jost:wght@400;500&display=swap">
<style>
:root{
  --blue:#3a52a4;
  --blue-text:#3b4c96;
  --ink:#1c1c1c;
  --body-gray:#6e6e6e;
  --header-bg:#e9eaec;
  --footer-bg:#414141;
  --footer-bar:#363636;
  --block-gray:#a5a5a5;
  --page-bg:#eceae6;
  --white:#ffffff;
}
*{box-sizing:border-box;margin:0;padding:0}
html,body{width:1200px;height:4004px;overflow:hidden;background:var(--page-bg)}
.site{position:absolute;left:234px;top:0;width:731px;height:4004px;background:var(--white);overflow:hidden;font-family:"Montserrat",sans-serif}

/* header */
.site-header{position:absolute;left:0;top:0;width:731px;height:115px;background:var(--header-bg)}
.brand{position:absolute;left:23px;top:28px;color:var(--blue-text);font-weight:500;line-height:1}
.brand-name{font-size:25px;letter-spacing:.5px;display:block}
.brand-sub{font-size:14px;letter-spacing:5.2px;display:block;margin-top:8px}
.menu-toggle{position:absolute;left:646px;top:28px;width:64px;height:58px;border:2px solid var(--blue);display:flex;flex-direction:column;justify-content:center;align-items:center;gap:8px}
.menu-toggle span{display:block;width:32px;height:2px;background:var(--blue)}

/* hero */
.hero{position:absolute;left:0;top:115px;width:731px;height:484px;background:linear-gradient(180deg,#dcdee1 0%,#c3c6ca 45%,#9ea2a7 70%,#3a3b40 86%,#1d1e22 100%)}
.hero-title{position:absolute;left:24px;top:86px;font-weight:900;font-size:39px;color:#111;letter-spacing:.3px}
.hero-sub{position:absolute;left:24px;top:148px;font-weight:600;font-size:26px;color:#111}

/* about */
.about-accent{position:absolute;left:23px;top:671px;width:343px;height:343px;background:var(--blue)}
.about-photo{position:absolute;left:0;top:1394px;width:731px;height:571px;background:linear-gradient(160deg,#3f5d3a 0%,#2f4a2c 35%,#7d7a66 55%,#405f38 75%,#27402a 100%)}
.about-card{position:absolute;left:51px;top:697px;width:629px;height:765px;background:var(--white);box-shadow:0 2px 8px rgba(0,0,0,.12);padding:38px 34px 0 31px}
.section-title{font-weight:600;font-size:36px;color:var(--blue-text);letter-spacing:.5px}
.rule{width:70px;height:3px;background:#9a9a9a;margin-top:16px}
.about-lead{margin-top:30px;font-size:22.5px;line-height:34px;color:var(--ink);font-weight:500;text-align:justify}
.about-body{margin-top:10px;font-size:21px;line-height:34.2px;color:var(--body-gray);font-weight:400;text-align:justify}
.about-more{position:absolute;right:28px;bottom:34px}

/* gallery */
.gallery-band{position:absolute;left:0;top:1965px;width:731px;height:315px;background:var(--blue)}
.gallery-accent{position:absolute;left:367px;top:2415px;width:345px;height:187px;background:var(--blue)}
.gallery-title{position:absolute;left:0;top:2026px;width:731px;text-align:center;color:var(--white);font-weight:600;font-size:36px;letter-spacing:1px}
.gallery-rule{position:absolute;left:330px;top:2072px;width:70px;height:3px;background:#c9cfe6}
.gallery-frame{position:absolute;left:51px;top:2123px;width:629px;height:426px;background:var(--white);padding:8px;box-shadow:0 1px 4px rgba(0,0,0,.15)}
.gallery-photo{width:100%;height:100%;background:linear-gradient(180deg,#9fc4de 0%,#bcd2df 16%,#5f7a4c 30%,#8a6b4e 55%,#6f5a45 75%,#54703f 100%)}
.gallery-nav{position:absolute;left:238px;top:2560px;display:flex;gap:16px}

/* footer */
.site-footer{position:absolute;left:0;top:2745px;width:731px;height:1259px;background:var(--footer-bg);font-family:"Jost",sans-serif;color:var(--white)}
.contact-accent{position:absolute;left:23px;top:2950px;width:241px;height:230px;background:var(--block-gray)}
.contact-card{position:absolute;left:51px;top:2675px;width:629px;height:462px;background:var(--blue);color:var(--white);font-family:"Jost",sans-serif}
.contact-brand{position:absolute;left:50px;top:50px;font-family:"Montserrat",sans-serif;font-weight:500;line-height:1;color:var(--white)}
.contact-brand .brand-name{font-size:34px;letter-spacing:.3px}
.contact-brand .brand-sub{font-size:18px;letter-spacing:6.4px;margin-top:10px}
.contact-item{position:absolute;left:49px;display:flex;align-items:center;gap:40px;font-size:25px;font-weight:500}
.contact-icon{width:56px;height:56px;border-radius:50%;background:var(--white);display:flex;align-items:center;justify-content:center;flex:none}
.footer-heading{position:absolute;font-size:26px;font-weight:500;letter-spacing:.3px}
.quick-links{position:absolute;left:53px;top:3296px;list-style:none}
.quick-links li{font-size:22px;line-height:48px;padding-left:22px;position:relative}
.quick-links li::before{content:"";position:absolute;left:0;top:22px;width:6px;height:6px;background:var(--white)}
.social{position:absolute;left:365px;top:3300px;list-style:none}
.social li{display:flex;align-items:center;gap:20px;height:80px;font-size:22px;margin-top:-12px}
.social li:first-child{margin-top:0}
.social .dot{width:56px;height:56px;border-radius:50%;background:#2b8fd9}
.newsletter-text{position:absolute;left:53px;top:3622px;width:560px;font-size:21.5px;line-height:30px}
.newsletter-input{position:absolute;left:51px;top:3697px;width:539px;height:62px;background:var(--white);border:none;padding-left:25px;font-family:"Jost",sans-serif;font-size:21px;color:#8a8a8a;display:flex;align-items:center}
.newsletter-button{position:absolute;left:51px;top:3781px;width:269px;height:60px;background:var(--blue);color:var(--white);font-family:"Jost",sans-serif;font-size:26px;font-weight:500;display:flex;align-items:center;justify-content:center}
.footer-bar{position:absolute;left:0;top:3917px;width:731px;height:87px;background:var(--footer-bar);font-family:"Jost",sans-serif;color:var(--white);font-size:19.5px;display:flex;align-items:center;padding-left:51px}
</style>
</head>
<body>
<div class="site">

  <header class="site-header">
    <div class="brand">
      <span class="brand-name">HARLOW STONEFIELD</span>
      <span class="brand-sub">CIVIL CONSTRUCTION</span>
    </div>
    <div class="menu-toggle"><span></span><span></span><span></span></div>
  </header>

  <section class="hero" role="img" aria-label="Grey evening sky over earthmoving machines shown as dark silhouettes on a ridge">
    <h1 class="hero-title">CIVIL CONSTRUTION FIRM</h1>
    <p class="hero-sub">In Business Since 20 Years</p>
  </section>

  <div class="about-accent"></div>
  <div class="about-photo" role="img" aria-label="Aerial view of a new road being cut through woodland beside a housing estate"></div>
  <section class="about-card">
    <h2 class="section-title">ABOUT US</h2>
    <div class="rule"></div>
    <p class="about-lead">Lorem ipsum dolor sit amet, consectetuer adipiscing elit, sed diammagna nonum my nibh euismod tincidunt ut laoreet dolore magna aliqua</p>
    <p class="about-body">Lorem ipsum dolor sit amet, consectetuer adipiscing elit, sed diam nonummy nibh euismod tincidunt ut laoreet dolore magna aliquam erat volutpat. Ut wisi enim ad minim veniam, quis nostrud exerci tation ullamcorper suscipit lobortis nisl ut aliquip ex ea commodo consequat. Lorem ipsum dolor sit amet, consectetuer adipiscing elit, sed diam nonummy nibh euismod tincidunt ut laoreet dolore magna aliquam erat volutpat. Ut wisi enim ad minim veniam, quis nostrud exerci tation ullamcorper suscipit lobortis nisl ut aliquip ex ea commodo consequat.</p>
    <svg class="about-more" width="46" height="24" viewBox="0 0 46 24"><path d="M2 12H42M32 3L43 12L32 21" fill="none" stroke="#111" stroke-width="2.6"/></svg>
  </section>

  <div class="gallery-band"></div>
  <div class="gallery-accent"></div>
  <h2 class="gallery-title">PHOTO GALLERY</h2>
  <div class="gallery-rule"></div>
  <div class="gallery-frame">
    <div class="gallery-photo" role="img" aria-label="Excavators digging a drainage trench beside houses under a clear sky"></div>
  </div>
  <div class="gallery-nav">
    <svg width="58" height="28" viewBox="0 0 58 28"><path d="M56 14H4M14 4L3 14L14 24" fill="none" stroke="#111" stroke-width="2.8"/></svg>
    <svg width="38" height="28" viewBox="0 0 38 28"><path d="M2 14H34M24 4L35 14L24 24" fill="none" stroke="#111" stroke-width="2.8"/></svg>
  </div>

  <footer class="site-footer"></footer>
  <div class="contact-accent"></div>
  <section class="contact-card">
    <div class="contact-brand">
      <span class="brand-name">HARLOW STONEFIELD</span>
      <span class="brand-sub">CIVIL CONSTRUCTION</span>
    </div>
    <div class="contact-item" style="top:183px">
      <span class="contact-icon"><svg width="24" height="30" viewBox="0 0 24 30"><path d="M12 1C6 1 2 5.5 2 11c0 7 10 18 10 18s10-11 10-18C22 5.5 18 1 12 1z" fill="#3a52a4"/><circle cx="12" cy="11" r="4" fill="#fff"/></svg></span>
      <span>48, Quarry Lane, Ridgeford, AB 204518</span>
    </div>
    <div class="contact-item" style="top:274px">
      <span class="contact-icon"><svg width="28" height="28" viewBox="0 0 28 28"><path d="M7 3l5 6-3 3c1.5 3 4 5.5 7 7l3-3 6 5-3 4C12 24 4 16 3 6z" fill="#3a52a4"/></svg></span>
      <span>+1 555 204 7781</span>
    </div>
    <div class="contact-item" style="top:361px;gap:34px">
      <span class="contact-icon"><svg width="30" height="24" viewBox="0 0 30 24"><rect x="2" y="3" width="26" height="18" fill="none" stroke="#3a52a4" stroke-width="3"/><path d="M2 4L15 14L28 4" fill="none" stroke="#3a52a4" stroke-width="3"/></svg></span>
      <span>info@harlowstonefield.com</span>
    </div>
  </section>

  <h3 class="footer-heading" style="left:53px;top:3238px;color:#fff;font-family:'Jost',sans-serif">QUICK LINKS</h3>
  <ul class="quick-links" style="color:#fff;font-family:'Jost',sans-serif">
    <li>Home</li><li>Project Gallery</li><li>Careers</li><li>Contact Us</li><li>Sitemap</li>
  </ul>
  <h3 class="footer-heading" style="left:367px;top:3238px;color:#fff;font-family:'Jost',sans-serif">FOLLOW US</h3>
  <ul class="social" style="color:#fff;font-family:'Jost',sans-serif">
    <li><span class="dot"></span>Facepage</li>
    <li><span class="dot"></span>Chirper</li>
    <li><span class="dot"></span>Linkpro</li>
  </ul>

  <h3 class="footer-heading" style="left:53px;top:3567px;color:#fff;font-family:'Jost',sans-serif">NEWSLETTER SIGN UP</h3>
  <p class="newsletter-text" style="color:#fff;font-family:'Jost',sans-serif">Subscribe to our newsletter to get the latest update to your inbox</p>
  <div class="newsletter-input">Enter your email address</div>
  <div class="newsletter-button">SUBSCRIBE</div>

  <div class="footer-bar">Copyright © 2019 Harlow Stonefield Civil Construction. All Rights Reserved.</div>
</div>
</body>
</html>
```